The Negative Effects of Childhood Abuse

I'm a 4th year psychology student and I need a project poster to present my research in 2 days. I have attached a power point file includes the content of the poster. You will find few pictures in the PP file as well, and you can choose whatever picture that fits with your design. feel free to use any pictures you prefer other than mine. I have also included a picture of poster samples so you can get a better idea. I want to see designs that use the colour blue and white. Please make sure to use the University logo in top of the poster, you will find it in the attachments files. Size of the poster is also included. I want the font to be readable (e.g., use 2o's for the body and 80's for headlines ) however, reference list should be in a smaller size unlike the rest of the body. I'm looking for simple designs with bright colours. Please be fast as possible I need it before Aug 13th.. No need to get 10 designs 3-5 would be fine.

Thank you!
Mirela

Industry/Entity Type

University

Colors
3176b5
0456a4
86acd3
fcfdfe

```html
<!DOCTYPE html>
<html lang="en">
<head>
<meta charset="utf-8">
<title>The Negative Effects of Childhood Abuse – Limitations and References</title>
<link rel="stylesheet" href="https://fonts.googleapis.com/css2?family=Source+Sans+3:ital,wght@0,300;0,400;1,400;1,600&display=swap">
<style>
  :root {
    --blue-mid: #3176b5;
    --blue-deep: #0456a4;
    --blue-light: #86acd3;
    --paper: #fcfdfe;
    --ink: #2a2a2a;
    --ink-body: #1f2a3a;
    --photo-dark: #3a1512;
    --photo-warm: #8a2a22;
  }
  * { margin: 0; padding: 0; box-sizing: border-box; }
  html, body { width: 1200px; height: 812px; overflow: hidden; background: var(--paper); }
  body { font-family: "Source Sans 3", sans-serif; color: var(--ink); }

  .poster { position: relative; width: 1200px; height: 812px; background: var(--paper); }

  .side-column { position: absolute; left: 0; top: 0; width: 390px; height: 812px; }
  .feature-photo {
    position: absolute; left: 0; top: 0; width: 370px; height: 150px;
    background: linear-gradient(120deg, var(--photo-dark) 0%, var(--photo-warm) 55%, #b98b78 100%);
  }
  .section-banner {
    position: absolute; left: 0; top: 178px; width: 380px; height: 96px;
    background: linear-gradient(90deg, var(--blue-deep) 0%, var(--blue-mid) 100%);
    display: flex; align-items: center; padding-left: 36px;
  }
  .section-banner h2 {
    font-weight: 300; font-size: 62px; color: var(--paper); letter-spacing: 0.5px;
  }
  .limitations-text {
    position: absolute; left: 36px; top: 308px; width: 345px;
    font-style: italic; font-weight: 600; font-size: 24px; line-height: 31px;
    color: var(--ink-body);
  }
  .limitations-text p + p { margin-top: 28px; }

  .references { position: absolute; left: 420px; top: 10px; width: 765px; height: 798px; }
  .references h2 { font-weight: 300; font-size: 64px; line-height: 72px; color: var(--ink); margin-bottom: 10px; }
  .reference-list { list-style: none; }
  .reference-list li {
    position: relative; padding-left: 58px; text-indent: -34px;
    font-style: italic; font-weight: 400; font-size: 15px; line-height: 19px;
    color: var(--ink); margin-bottom: 8px;
  }
  .reference-list li::before {
    content: ""; position: absolute; left: 0; top: 6px;
    width: 8px; height: 8px; border-radius: 50%; background: var(--ink);
  }
</style>
</head>
<body>
<main class="poster">
  <section class="side-column">
    <div class="feature-photo" role="img" aria-label="Photograph of a young person in a red top"></div>
    <div class="section-banner"><h2>Limitations</h2></div>
    <div class="limitations-text">
      <p>Limited time made it difficult to recruit youth from the general population, so findings and protective factors are hard to generalize. Future studies’ should include adolescents who may be at risk but who may not seek help from clinicians.</p>
      <p>Future work should measure the frequency and severity of abuse to provide more detail on how childhood abuse with depression is linked.</p>
    </div>
  </section>

  <section class="references">
    <h2>References</h2>
    <ul class="reference-list">
      <li>Averin, C. M., Lindqvist-Rowan, J., Baxter, D., &amp; O’Malley-Sutton, L. (2005). Single and multiple forms of maltreatment: A look at the lasting effects of child abuse. Journal of Youth Harm Studies, 11, 29–52. doi:10.5500/jyhs.2005.0112</li>
      <li>Carrington-Hale, C., Calder, A. R., Morrow-Clarke, D., Castellan, D., Creed, N. R., &amp; Rothmann, F. A. (2008). Early maltreatment and the growth of relational and physical aggression: Why gender matters. Northfield Review of Child Growth, 79, 1736-1751. doi:10.5500/nrcg.2008.0417</li>
      <li>Fenwick, J., Farley, L., &amp; Conroy, D. (2010). Child abuse and aggression among children with serious emotional needs. Journal of Applied Youth Psychology, 39(1), 25–34.</li>
      <li>Grell, B. E., &amp; Abbas, J. Z. (2008). Emotional abuse, verbal victimization, and the growth of negative thinking styles and low mood in children. Cognition and Mood Quarterly, 32, 161–176. doi:10.5500/cmq.2008.0321</li>
      <li>Guerrero, A., Boland, M.H., Kwan, H.H., Giorgi, K., Dunmore, L., &amp; MacLeod, H.L. (2012). Childhood and family influences on depression, long-term physical illness, and their overlap: results from the Lakeshore Family Health Survey. Clinical Mind Reports 46, 1475–1482. http://dx.doi.org.proxy.library.northfield.ca/10.5500/cmr.2012.0846</li>
      <li>Hadad-Yassin, M. M., &amp; de Silveira, P. (2008). Rates and psychological effects of exposure to family violence among coastal university students. Family Safety Review, 32(10), 994-1002</li>
      <li>Hollenbeck, T. I., Marsh, W. A., Kessler, R., Lenz, L. J., Hawley, J. D., &amp; Abel, R. D (2004). Routes from physical abuse in childhood to partner violence in early adulthood. Studies in Interpersonal Conflict, 19(2), 123–136. doi:10.5500/sic.2004.1902</li>
      <li>Jessop, R., Dunmire, K.L., Ndlovu, M., Jali, N., &amp; Purcell, A. (2010). Links between childhood adversity and depression, substance use and new infections among rural youth. Family Safety Review, 34, 833–841.</li>
      <li>Jourdan, E. N., McAllister, R., Sloane, A. M., Hayward, R. E., &amp; Galindo, E. (2008). Child abuse where domestic violence is present: Rates, causes, and practice. Studies in Interpersonal Conflict, 23, 221–235. doi:10.5500/sic.2008.2302</li>
      <li>Kendall, R., Bellamy, K. M., &amp; Guillot, J. M. (2012). How child abuse history, trauma symptoms, and anger arousal shape dating violence among college women. Home and Harm Journal, 27, 165–175. doi:10.5500/hhj.2012.0275</li>
      <li>Kwon, J., &amp; Castellan, D. (2006). Long-term paths of self-esteem and depressive symptoms among maltreated and non maltreated children. Northfield Review of Child Growth, 77, 624–639. doi:10.5500/nrcg.2006.0894</li>
      <li>Lin, R., Albury, L., Abrams, L., Iacobelli, B., &amp; Whitfield, W. (2009). Emotional maltreatment and depression: Predicting later depressive episodes. Mood Disorders Bulletin, 26(2), 174-181.</li>
      <li>Lang, M., &amp; Wilkes, S. K. (1997). Repeated maltreatment experiences and adolescent behaviour problems. Growth and Risk Journal, 9, 131–149.</li>
    </ul>
  </section>
</main>
</body>
</html>
```